Vortelan d.o.o. needes a web site design

We are a company dealing with automatic doors, industrial doors, roller shutters, access control systems.
We would like to get a design which is clean and neat, and here are some sites which work with similar products. These designs are some we like, but of course, I am looking for a design which is unique. We usually use grey and red colours, which you can see on www.vortelan.ba .
The sites we like are:
http://www.plexawin.com/gb/
http://www.brunosteca.it/eng/
http://faswoodportamel.com/

You have to understand, that we have 4 different groups of products, which are main groups. I would like if those 4 groups somehow could be in different colours. (Maybe "zuvex" colours), in order to separate the groups in some way.

Attached you have web site structure.

If any questions, please contact me.
Edvin

Target Market(s)

Bosnian market. Aluminium and PVC doors and window market, Construction companies, Supermarkets-Retail, Gas stations, Banks, Food industry, Heavy industry.

Industry/Entity Type

It Company

Contact Information for Business Card

I have attached our current business card in PDF. I weould like english on one side, bosnian on other side.

Logo Text

Vortelan is the name of the company, our core business is automation!

Number of Pages Required

5+ page

Font styles to use
Sans Serif

Colors
ec1f27
0792cd
9bcb3c
ffc214
ffffff

```html
<!DOCTYPE html>
<html lang="bs">
<head>
<meta charset="utf-8">
<title>Vortelan d.o.o.</title>
<link rel="stylesheet" href="https://fonts.googleapis.com/css2?family=Montserrat:wght@400;500;600&family=Arimo:wght@400;700&display=swap">
<style>
:root{
  --red:#ec1f27;
  --blue:#0792cd;
  --green:#9bcb3c;
  --yellow:#ffc214;
  --white:#ffffff;
  --ink:#444;
  --ink-soft:#6d6d6d;
  --muted:#8a8a8a;
  --line:#cfcfcf;
  --page:#f4f4f4;
}
*{margin:0;padding:0;box-sizing:border-box}
html,body{width:1111px;height:1200px;overflow:hidden}
body{position:relative;background:var(--page);font-family:"Arimo",Arial,sans-serif;color:var(--ink)}
.abs{position:absolute}

/* header */
.site-header{position:absolute;left:0;top:0;width:1111px;height:109px;background:var(--white)}
.header-rule{position:absolute;left:0;top:71px;width:1111px;height:1px;background:#555}
.brand{position:absolute;left:180px;top:60px;font-family:"Montserrat",sans-serif;font-weight:600;font-size:22px;color:var(--red);letter-spacing:1px}
.social{position:absolute;top:47px;left:843px;display:flex;gap:17px}
.social span{width:9px;height:9px;border-radius:50%;background:#b5b5b5}
.main-nav{position:absolute;top:78px;left:0;font-size:12.5px;color:var(--ink)}
.main-nav a{position:absolute;white-space:nowrap;text-decoration:none;color:inherit}
.main-nav .active{color:var(--red)}

/* hero */
.hero{position:absolute;left:0;top:109px;width:1111px;height:414px;background:linear-gradient(180deg,#9a9590 0%,#c7cbcd 45%,#8c8782 80%,#6f6a66 100%)}
.hero-title{position:absolute;left:181px;top:153px;width:304px;height:41px;background:var(--red);color:var(--white);font-family:"Montserrat",sans-serif;font-size:19px;letter-spacing:2px;padding:10px 0 0 31px}
.hero-bar{position:absolute;left:180px;top:201px;width:450px;height:4px;background:var(--red)}
.hero-text{position:absolute;left:180px;top:205px;width:450px;height:66px;background:rgba(90,90,92,.9);color:var(--white);font-family:"Montserrat",sans-serif;font-size:14.5px;line-height:24px;padding:7px 0 0 33px}
.hero-arrow{position:absolute;top:200px}
.hero-dots{position:absolute;top:357px;left:530px;display:flex;gap:5px}
.hero-dots span{width:10px;height:10px;border-radius:50%;border:1.5px solid var(--white)}
.hero-dots .on{background:var(--red);border-color:var(--red)}

/* categories */
.categories{position:absolute;left:179px;top:549px;height:76px;display:flex}
.category{height:76px;color:var(--white);font-family:"Montserrat",sans-serif;padding:23px 0 0 20px}
.category h3{font-size:11.5px;font-weight:500;letter-spacing:.8px}
.category p{font-size:9.5px;margin-top:9px}
.cat-red{width:193px;background:var(--red)}
.cat-blue{width:193px;background:var(--blue)}
.cat-green{width:174px;background:var(--green)}
.cat-yellow{width:193px;background:var(--yellow)}

.section-title{position:absolute;top:667px;font-family:"Montserrat",sans-serif;font-size:14.5px;color:var(--ink-soft);letter-spacing:.4px}

/* product cards */
.product{position:absolute;top:705px;width:239px;height:259px;background:var(--white)}
.product .photo{height:138px}
.product h4{font-family:"Montserrat",sans-serif;font-weight:500;font-size:11.5px;margin:20px 0 0 24px;color:var(--ink)}
.product p{font-size:11.5px;line-height:18px;margin:11px 20px 0 24px;color:var(--ink)}
.product .more{font-size:8px;margin:12px 0 0 24px;color:var(--ink);letter-spacing:.2px}

/* news */
.news{position:absolute;left:693px;width:240px;border-left:2px solid var(--line);padding-left:10px}
.news .meta{font-size:9.5px;color:var(--muted);margin-top:-7px;margin-left:-10px;padding-left:10px}
.news h5{font-weight:400;font-size:12.5px;line-height:17.6px;color:var(--ink-soft);margin-top:13px}
.news .by{font-size:9.5px;color:var(--muted);margin-top:25px}

/* footer */
.site-footer{position:absolute;left:0;top:1027px;width:1111px;height:173px;border-top:1px solid var(--line);background:var(--page)}
.footer-brand{position:absolute;left:180px;top:70px;font-family:"Montserrat",sans-serif;font-weight:600;font-size:17px;color:var(--red);letter-spacing:.8px}
.copyright{position:absolute;left:180px;top:106px;width:120px;text-align:center;font-family:"Montserrat",sans-serif;font-size:9.5px;line-height:18px;color:var(--ink-soft)}
.footer-rule{position:absolute;top:36px;width:1px;height:123px;background:var(--line)}
.footer-links{position:absolute;top:35px;list-style:none;font-weight:700;font-size:10.5px;color:var(--ink-soft)}
.footer-links li{height:24px}
.contact-title{position:absolute;left:692px;top:34px;font-family:"Montserrat",sans-serif;font-size:14px;color:var(--ink)}
.contact-lines{position:absolute;left:693px;top:67px;list-style:none;font-size:11.5px;color:var(--ink)}
.contact-lines li{height:24px}
.contact-lines b{font-weight:700}
</style>
</head>
<body>

<header class="site-header">
  <div class="header-rule"></div>
  <div class="brand">Vortelan d.o.o.</div>
  <div class="social"><span></span><span></span><span></span><span></span></div>
  <nav class="main-nav">
    <a class="active" style="left:613px">company</a>
    <a style="left:705px">products
      <svg width="11" height="7" viewBox="0 0 11 7" style="margin-left:6px"><path d="M1 1l4.5 4.5L10 1" fill="none" stroke="#777" stroke-width="1.2"/></svg></a>
    <a style="left:807px">reference</a>
    <a style="left:892px">contact</a>
  </nav>
</header>

<section class="hero" role="img" aria-label="Photo of an automatic glass sliding door entrance in a modern lobby">
  <div class="hero-title">NOVA WEB STRANICA</div>
  <div class="hero-bar"></div>
  <div class="hero-text">u toku su radovi na novoj web prezentaciji naših usluga,<br>uskoro smo ponovo sa vama</div>
  <svg class="hero-arrow" style="left:20px" width="18" height="32" viewBox="0 0 18 32"><path d="M16 1L2 16l14 15" fill="none" stroke="#fff" stroke-width="2"/></svg>
  <svg class="hero-arrow" style="left:1075px" width="18" height="32" viewBox="0 0 18 32"><path d="M2 1l14 15L2 31" fill="none" stroke="#fff" stroke-width="2"/></svg>
  <div class="hero-dots"><span></span><span class="on"></span><span></span><span></span></div>
</section>

<div class="categories">
  <div class="category cat-red"><h3>AUTOMATSKA VRATA</h3><p>view all products</p></div>
  <div class="category cat-blue"><h3>INDUSTRIJSKA VRATA</h3><p>view all products</p></div>
  <div class="category cat-green"><h3>ROLO VRATA</h3><p>view all products</p></div>
  <div class="category cat-yellow"><h3>KONTROLA PRISTUPA</h3><p>view all products</p></div>
</div>

<h2 class="section-title" style="left:181px">FEATURED PRODUCT</h2>
<h2 class="section-title" style="left:692px">IN THE NEWS</h2>

<article class="product" style="left:180px">
  <div class="photo" role="img" aria-label="Photo of a warehouse facade with loading dock doors" style="background:linear-gradient(180deg,#eef1f4 0%,#5d6470 40%,#3f4550 70%,#b9bcbf 100%)"></div>
  <h4>Pretovarni mostovi</h4>
  <p>u toku su radovi na novoj web prezent-<br>aciji naših usluga, uskoro</p>
  <div class="more">VIEW PRODUCT</div>
</article>
<article class="product" style="left:436px">
  <div class="photo" role="img" aria-label="Photo of a closed metal roller shutter door" style="background:linear-gradient(90deg,#c9a9ad 0%,#d4d6d8 20%,#b5b8bb 60%,#7d7f82 100%)"></div>
  <h4>Pretovarni mostovi</h4>
  <p>u toku su radovi na novoj web prezent-<br>aciji naših usluga, uskoro</p>
  <div class="more">VIEW PRODUCT</div>
</article>

<article class="news" style="top:714px">
  <div class="meta">August 26, 2015 | On the News | Meridane</div>
  <h5>Vortelan on Meridane: Hedge Funds Suddenly Find Real Money Is Back in Argentina’s Debt</h5>
  <div class="by"><i>By</i> Lena Varkovic</div>
</article>
<article class="news" style="top:858px">
  <div class="meta">August 26, 2015 | On the News | Meridane</div>
  <h5>Vortelan on Meridane: Hedge Funds Suddenly Find Real Money Is Back in Argentina’s Debt</h5>
  <div class="by"><i>By</i> Lena Varkovic</div>
</article>

<footer class="site-footer">
  <div class="footer-brand">Vortelan d.o.o.</div>
  <div class="copyright">© 2008-2016<br>Vortelan d.o.o. Krasno</div>
  <div class="footer-rule" style="left:355px"></div>
  <div class="footer-rule" style="left:499px"></div>
  <div class="footer-rule" style="left:675px"></div>
  <ul class="footer-links" style="left:373px"><li>Company</li><li>Reference</li><li>Contact</li></ul>
  <ul class="footer-links" style="left:521px"><li>Automatska Vrata</li><li>Industrijska Vrata</li><li>Rolo Vrata</li><li>Kontrola Pristupa</li></ul>
  <h3 class="contact-title">CONTACT</h3>
  <ul class="contact-lines">
    <li>Javorova Brigada BB,</li>
    <li>74300 KRASNO</li>
    <li><b>Call: +387 55 410 320</b></li>
    <li><b>Fax: +387 55 410 321</b></li>
  </ul>
</footer>

</body>
</html>
```